Solar company mail box flyer design

We are a solar installation company and we currently need a DL flyer design for mailbox distribution. The front page need to mention that the government rebate is going to be reduced from the first day of the next year. Also, it need to mentioned that $100 discount available for any customer who show us this flyer. We will also need to have some solar panels and inverters demonstrated on the front page.

I have attached some similar flyers for reference purpose.

It Company

```html
<!DOCTYPE html>
<html lang="en">
<head>
<meta charset="utf-8">
<title>Brightway Solar – DL Flyer</title>
<link href="https://fonts.googleapis.com/css2?family=Lato:wght@400;700&family=Montserrat:wght@700;800&family=Oswald:wght@500&display=swap" rel="stylesheet">
<style>
  :root{
    --orange:#f0a122;
    --navy:#1c2a5c;
    --blue:#1b5fa8;
    --ink:#1a1a1a;
    --arc:#3a3a3a;
    --footer-edge:#4a4a4a;
    --page:#e9e6e1;
    --white:#ffffff;
  }
  *{box-sizing:border-box;margin:0;padding:0}
  html,body{width:1200px;height:1200px;overflow:hidden;background:var(--page)}
  .flyer{
    position:absolute;left:335px;top:40px;width:530px;height:1121px;
    background:var(--white);overflow:hidden;
    box-shadow:0 6px 18px rgba(0,0,0,.18);
    font-family:"Lato",sans-serif;color:var(--ink);
  }
  .hero{position:absolute;left:0;top:0;width:530px;height:640px}
  .logo{
    position:absolute;top:48px;left:0;width:100%;text-align:center;
    font-family:"Montserrat",sans-serif;font-weight:800;font-size:40px;color:var(--ink);
    letter-spacing:1px;
  }
  .badge{
    position:absolute;left:321px;top:403px;width:172px;height:172px;border-radius:50%;
    background:var(--orange);border:3px solid var(--white);
    box-shadow:0 0 0 2px var(--orange);
    display:flex;flex-direction:column;align-items:center;justify-content:center;
    font-family:"Oswald",sans-serif;font-weight:500;color:#2a2a2a;line-height:1;
  }
  .badge__amount{font-size:60px}
  .badge__label{font-size:32px;margin-top:4px}
  .tab{
    position:absolute;left:0;top:542px;width:180px;height:29px;background:var(--orange);
    clip-path:polygon(0 0,100% 0,92% 100%,0 100%);
    font-family:"Montserrat",sans-serif;font-weight:800;font-size:20px;color:var(--blue);
    padding-left:38px;line-height:31px;
  }
  .copy{position:absolute;left:33px;width:475px;font-size:16px;line-height:20px;white-space:nowrap}
  .copy--intro{top:598px}
  .copy--save{top:680px}
  .copy--choice{top:738px}
  .copy--draw{top:792px;left:30px}
  .copy--rebate{top:843px;left:30px;font-size:15px;line-height:18px;font-weight:700;color:var(--navy)}
  .rule{position:absolute;left:42px;width:326px;height:1px;background:var(--orange)}
  .rule--a{top:727px}.rule--b{top:781px}
  .cta{position:absolute;left:20px;top:872px;width:200px;text-align:center;font-family:"Montserrat",sans-serif;font-weight:700}
  .cta__head{font-size:24px;line-height:43px;color:var(--ink)}
  .cta__call{font-size:23px;color:var(--navy);margin-top:6px}
  .cta__phone{font-size:23px;color:var(--ink);margin-top:8px}
  .product{position:absolute;left:247px;top:873px;width:266px;height:192px}
  .footer{
    position:absolute;left:0;top:1074px;height:38px;background:var(--orange);
    border-bottom:9px solid var(--footer-edge);box-sizing:content-box;
    display:flex;align-items:center;justify-content:space-between;padding:0 18px 0 38px;
    font-size:16px;color:var(--ink);width:474px;
  }
  .footer__item{display:flex;align-items:center;gap:5px}
  .footer__item svg{flex:none}
</style>
</head>
<body>
<main class="flyer">
  <svg class="hero" viewBox="0 0 530 640" width="530" height="640">
    <defs>
      <linearGradient id="photoTone" x1="0" y1="0" x2="1" y2="1">
        <stop offset="0" stop-color="#cfe1f0"/>
        <stop offset="0.45" stop-color="#9fb7c9"/>
        <stop offset="0.7" stop-color="#5d7f4c"/>
        <stop offset="1" stop-color="#2f4f8f"/>
      </linearGradient>
    </defs>
    <rect x="0" y="70" width="530" height="470" fill="url(#photoTone)" role="img" aria-label="Photo of a smiling installer in a hard hat fitting solar panels on a roof, with trees and sky behind"/>
    <path d="M0,88 Q265,240 530,88 L530,100 Q265,252 0,100 Z" fill="#8a9fd0"/>
    <path d="M0,0 H530 V80 Q265,226 0,80 Z" fill="var(--orange)"/>
    <path d="M0,464 Q224,562 530,429 L530,640 L0,640 Z" fill="var(--white)"/>
    <path d="M0,464 Q224,562 530,429" fill="none" stroke="var(--arc)" stroke-width="4"/>
  </svg>
  <div class="logo">YOUR LOGO</div>

  <div class="badge">
    <span class="badge__amount">$100</span>
    <span class="badge__label">DISCOUNT</span>
  </div>

  <div class="tab">WHY WAIT</div>

  <p class="copy copy--intro">Going solar has never never been eaiser and more effordable.<br>callus today for your free solar evalution and get starter with a<br>brighterfuture tomorrow</p>
  <p class="copy copy--save">Did you know you can save at least $400 a quarter on your<br>power bill with solar?</p>
  <div class="rule rule--a"></div>
  <p class="copy copy--choice">Electricity company or back in your pocket? Choice is<br>yours!</p>
  <div class="rule rule--b"></div>
  <p class="copy copy--draw">Choose Brightway Solar for your chanceto win 5 Harbor<br>Bros &amp;</p>
  <p class="copy copy--rebate">Government rebate reduces from 1 January next year!</p>

  <div class="cta">
    <p class="cta__head">FOR MORE<br>DETAILS</p>
    <p class="cta__call">CALL US NOW</p>
    <p class="cta__phone">1300 555 019</p>
  </div>

  <svg class="product" viewBox="0 0 266 192" role="img" aria-label="Product photo of three solar inverters in white, blue and red">
    <rect x="60" y="0" width="206" height="172" fill="#f1f2f3"/>
    <rect x="0" y="66" width="112" height="118" fill="#2e5aa0"/>
    <rect x="112" y="104" width="68" height="78" fill="#d92b2b"/>
  </svg>

  <footer class="footer">
    <span class="footer__item">
      <svg width="16" height="12" viewBox="0 0 16 12"><rect x="0.5" y="0.5" width="15" height="11" fill="none" stroke="#1a1a1a"/><path d="M0.5,0.5 L8,7 L15.5,0.5" fill="none" stroke="#1a1a1a"/></svg>
      info@brightwaysolar.com.au
    </span>
    <span class="footer__item">
      <svg width="20" height="20" viewBox="0 0 20 20"><circle cx="10" cy="10" r="8" fill="none" stroke="#1a1a1a" stroke-width="1.4"/><ellipse cx="10" cy="10" rx="3.5" ry="8" fill="none" stroke="#1a1a1a" stroke-width="1.2"/><path d="M2,10 H18 M3.5,6 H16.5 M3.5,14 H16.5" stroke="#1a1a1a" stroke-width="1.2"/></svg>
      www.BrightwaySolar.com.au
    </span>
  </footer>
</main>
</body>
</html>
```